Bully breed rescue website

I need a website for my bully breed rescue. We rescue bully breeds from up and down the east coast of the United States and train them as service dogs for people with limited mobility disabilities. I don't want a lot of white space. I want it to be modern and slick and colorful and still look professional. I want it to be different and have a lot of wow factor. I linked a copy of my logo.

Number of Pages Required

5+ page

Font styles to use
Sans Serif

Colors

Designer to choose colors to be used in the design.

Requirements
Must have
• Moving aspects. Blog and ecommerce.
• 1.) Home page
• 2.) Services- something modular
• 3.) About US
• 4.) Blog
• 5.) Application page
• 6.) Donation page
• 7.) Contact Us
Nice to have
• Large Slider of photos on home page
• vertical menu bar
Should not have
• Lots of white space. Dont want it to look like a template or any other site

```html
<!DOCTYPE html>
<html lang="en">
<head>
<meta charset="utf-8">
<title>Gentle Giants Rescue</title>
<link href="https://fonts.googleapis.com/css2?family=Roboto:wght@400;500;700&display=swap" rel="stylesheet">
<style>
  :root {
    --yellow: #f7d23e;
    --button-yellow: #f4cd3b;
    --ink: #2a2a2a;
    --white: #ffffff;
    --grass-dark: #3f7a23;
    --grass-light: #8fc25a;
    --coat: #e9e2da;
    --paw-red: #e52a2a;
    --paw-green: #4e9a1c;
    --paw-yellow: #f3c51b;
  }
  * { margin: 0; padding: 0; box-sizing: border-box; }
  html, body { width: 1200px; height: 1025px; overflow: hidden; }
  body { font-family: "Roboto", Arial, sans-serif; background: var(--white); position: relative; }

  .hero { position: absolute; left: 0; top: 0; width: 923px; height: 1025px; overflow: hidden; }
  .hero-photo {
    position: absolute; left: 0; top: 0; width: 923px; height: 770px;
    background:
      radial-gradient(ellipse 380px 300px at 640px 260px, #d9cfc4 0%, rgba(217,207,196,0.6) 55%, rgba(217,207,196,0) 100%),
      radial-gradient(ellipse 300px 200px at 250px 150px, rgba(240,240,235,0.85), rgba(240,240,235,0) 100%),
      linear-gradient(180deg, #c9d7b4 0%, var(--grass-light) 45%, var(--grass-dark) 100%);
  }
  .hero-logo { position: absolute; left: 42px; top: 70px; display: flex; align-items: center; gap: 8px; }
  .brand-dot { width: 14px; height: 14px; border-radius: 50%; background: var(--ink); flex: none; }
  .brand-name { font-weight: 700; font-size: 18px; color: var(--ink); white-space: nowrap; }

  .slider-arrow { position: absolute; left: 40px; top: 372px; }
  .hero-title {
    position: absolute; left: 0; width: 1195px; top: 340px; text-align: center;
    font-weight: 500; font-size: 66px; color: var(--white); letter-spacing: -0.5px;
  }
  .donate-button {
    position: absolute; left: 429px; top: 442px; width: 344px; height: 76px;
    border-radius: 38px; background: var(--button-yellow); color: var(--white);
    font-weight: 500; font-size: 27px; display: flex; align-items: center; justify-content: center;
  }
  .slider-dots { position: absolute; left: 514px; top: 645px; display: flex; gap: 5px; }
  .slider-dots span { width: 30px; height: 6px; border-radius: 3px; background: rgba(255,255,255,0.55); }
  .slider-dots span.active { background: var(--white); }

  .wave { position: absolute; left: 0; top: 660px; }

  .about-title {
    position: absolute; left: 0; width: 1200px; top: 774px; text-align: center;
    font-weight: 500; font-size: 33px; color: #222;
  }
  .pillar { position: absolute; font-size: 28px; color: #222; white-space: nowrap; }
  .paw { position: absolute; border-radius: 50%; }
  .paw.red { background: var(--paw-red); }
  .paw.green { background: var(--paw-green); }
  .paw.yellow { background: var(--paw-yellow); }

  .sidebar {
    position: absolute; left: 923px; top: 0; width: 277px; height: 1025px;
    background: var(--yellow); z-index: 2;
  }
  .sidebar-logo { position: absolute; left: 0; width: 277px; top: 138px; display: flex; justify-content: center; align-items: center; gap: 8px; }
  .sidebar-logo .brand-name { font-size: 20px; }
  .menu { list-style: none; position: absolute; left: 0; width: 277px; top: 280px; }
  .menu li {
    height: 82.4px; text-align: center; font-weight: 500; font-size: 23px; color: var(--ink);
  }
  .social { position: absolute; left: 0; width: 277px; top: 866px; display: flex; justify-content: center; gap: 16px; }
  .social span { width: 34px; height: 34px; border-radius: 50%; background: var(--white); }
  .copyright { position: absolute; left: 0; width: 277px; top: 924px; text-align: center; font-size: 15px; color: var(--ink); }
</style>
</head>
<body>
  <section class="hero">
    <div class="hero-photo" role="img" aria-label="Photo of a bulldog lying in green grass on a leash"></div>
    <div class="hero-logo"><span class="brand-dot"></span><span class="brand-name">Gentle Giants</span></div>
    <svg class="slider-arrow" width="26" height="44" viewBox="0 0 26 44" aria-hidden="true">
      <polyline points="20,4 6,22 20,40" fill="none" stroke="#fff" stroke-width="6" stroke-linecap="round" stroke-linejoin="round"/>
    </svg>
    <h1 class="hero-title">GENTLE GIANTS</h1>
    <div class="donate-button">DONATE NOW!</div>
    <div class="slider-dots"><span class="active"></span><span></span><span></span><span></span><span></span></div>
    <svg class="wave" width="923" height="365" viewBox="0 0 923 365" aria-hidden="true">
      <path d="M0,82 C120,30 260,0 380,12 C560,30 700,80 923,108 L923,365 L0,365 Z" fill="#fff"/>
    </svg>

    <h2 class="about-title">WHO WE ARE?</h2>

    <span class="paw red" style="left:214px;top:886px;width:44px;height:44px"></span>
    <span class="paw green" style="left:155px;top:958px;width:46px;height:46px"></span>
    <span class="pillar" style="left:225px;top:956px">OUR MISSION</span>
    <span class="paw yellow" style="left:434px;top:946px;width:48px;height:48px"></span>

    <span class="paw red" style="left:778px;top:886px;width:44px;height:44px"></span>
    <span class="paw green" style="left:719px;top:958px;width:46px;height:46px"></span>
    <span class="pillar" style="left:802px;top:956px">OUR VISION</span>
  </section>

  <nav class="sidebar">
    <div class="sidebar-logo"><span class="brand-dot"></span><span class="brand-name">Gentle Giants</span></div>
    <ul class="menu">
      <li>HOME PAGE</li>
      <li>SERVICES</li>
      <li>ABOUT US</li>
      <li>BLOG</li>
      <li>APPLICATION</li>
      <li>DONATION</li>
      <li>CONTACT US</li>
    </ul>
    <div class="social"><span></span><span></span><span></span><span></span></div>
    <p class="copyright">© 2018 | GENTLE GIANTS RESCUE</p>
  </nav>
</body>
</html>
```